Travel Poster Design Project

A poster design for a specific Adventure Travel Journey to Ladakh India. The journey it will be promoting is a 2 week trekking and cultural tour through Ladakh passing over 2 mountain passes in excess of 5000 meters.

Dates are July and August each year

Brand Name is Farwind Treks

We do inspiring unique journeys in a small select number of locations around the world. Ladakh is also known as Little Tibet and has a buddhist culture

We have a logo already to use and we also have a range of photos online for you to select from. They can be seen at http://images.brookpaddle.example/FarwindTreks then click on Ladakh

Target Market(s)

Adventure travel people 30-55 poster will be displayed in our rafting retail base so will be seen by target market

Industry/Entity Type

Travel

Requirements
Must have
• website address www.farwindtreks.example
Phone Number 01632 960418
email info@farwindtreks.example
Pictures
small legal note along the bottom, saying Farwind Treks is a brand name of Torrent Ridge River Sports LLP
Nice to have
• Lots of inspiring photos and colour
Should not have
• named dates

```html
<!DOCTYPE html>
<html lang="en">
<head>
<meta charset="utf-8">
<title>Adventure Travel Journey to Ladakh India – Farwind Treks</title>
<link href="https://fonts.googleapis.com/css2?family=Cormorant+Garamond:ital,wght@1,500;1,600&family=Kaushan+Script&family=Fenix&family=Tinos&display=swap" rel="stylesheet">
<style>
  :root {
    --sky-top: #8ab6e3;
    --sky-bottom: #c9cfea;
    --navy: #1f1f66;
    --orange: #ec5a14;
    --ink: #111111;
    --ornament-grey: #a9a9a9;
    --frame-white: #ffffff;
    --frame-black: #0c0c0c;
  }
  * { margin: 0; padding: 0; box-sizing: border-box; }
  html, body { width: 848px; height: 1200px; overflow: hidden; background: #ffffff; }
  .poster {
    position: relative;
    width: 848px;
    height: 1200px;
    overflow: hidden;
    background: linear-gradient(180deg, var(--sky-top) 0%, #a9c3ea 45%, var(--sky-bottom) 100%);
    font-family: "Fenix", Georgia, serif;
    color: var(--ink);
  }

  /* brand */
  .brand-dot { position: absolute; left: 50px; top: 45px; width: 104px; height: 104px;
    border-radius: 50%; background: var(--ink); }
  .brand-name { position: absolute; left: 207px; top: 76px;
    font-family: "Fenix", Georgia, serif; font-size: 28px; color: var(--ink); white-space: nowrap; }

  /* tour summary tag */
  .summary-shape { position: absolute; left: 555px; top: 10px; width: 250px; height: 150px;
    background: var(--ornament-grey); transform: rotate(30deg); border-radius: 18px; opacity: .85; }
  .summary-text { position: absolute; left: 550px; top: 58px; width: 250px;
    transform: rotate(30deg); text-align: center;
    font-family: "Tinos", "Times New Roman", serif; font-size: 15px; line-height: 17px; color: var(--ink); }

  /* headline */
  .headline-top { position: absolute; left: 78px; top: 165px;
    font-family: "Cormorant Garamond", Georgia, serif; font-style: italic; font-weight: 500;
    font-size: 73px; color: var(--navy); letter-spacing: 1px; white-space: nowrap; }
  .headline-to { position: absolute; left: 131px; top: 276px;
    font-family: "Cormorant Garamond", Georgia, serif; font-style: italic; font-weight: 500;
    font-size: 64px; color: var(--navy); }
  .headline-place { position: absolute; left: 205px; top: 236px;
    font-family: "Kaushan Script", cursive; font-size: 102px; color: var(--orange); white-space: nowrap; }
  .season { position: absolute; left: 423px; top: 360px;
    font-family: "Cormorant Garamond", Georgia, serif; font-style: italic; font-weight: 600;
    font-size: 35px; color: var(--navy); white-space: nowrap; }

  /* photo frames */
  .photo { position: absolute; padding: 12px; background: var(--frame-white); }
  .photo.dark { background: var(--frame-black); padding: 11px; }
  .photo-fill { width: 100%; height: 100%; }
  .photo-mosque { left: 54px; top: 459px; width: 246px; height: 272px; transform: rotate(-21deg); }
  .photo-mosque .photo-fill { background: linear-gradient(180deg, #3f79cf 0%, #a9c6ea 45%, #d9d0bc 70%, #8c7a63 100%); }
  .photo-chorten { left: 312px; top: 432px; width: 216px; height: 288px; transform: rotate(8deg); }
  .photo-chorten .photo-fill { background: linear-gradient(180deg, #4a86d4 0%, #c9dcf2 55%, #a45a3a 80%, #d8cbb4 100%); }
  .photo-gateway { left: 542px; top: 459px; width: 213px; height: 296px; }
  .photo-gateway .photo-fill { background: linear-gradient(90deg, #4a3a2a 0%, #c8bba4 30%, #e8e1d2 55%, #b4a890 75%, #3e3024 100%); }
  .photo-peak { left: 121px; top: 704px; width: 302px; height: 212px; }
  .photo-peak .photo-fill { background: linear-gradient(180deg, #b8c6d6 0%, #dfe3e8 35%, #6f7277 65%, #3f4246 100%); }
  .photo-temple { left: 430px; top: 708px; width: 310px; height: 190px; transform: rotate(-10deg); }
  .photo-temple .photo-fill { background: linear-gradient(135deg, #c93b3b 0%, #3f7f6b 35%, #e6d6a8 60%, #2f5d9a 85%, #b8333a 100%); }

  /* contact */
  .wheel-mark { position: absolute; left: 68px; top: 1010px; width: 122px; height: 122px;
    border-radius: 50%; background: #3e3e3e; }
  .contact { position: absolute; left: 278px; top: 1022px; list-style: none;
    font-family: "Fenix", Georgia, serif; font-size: 29px; font-weight: 700; line-height: 36px;
    color: var(--ink); white-space: nowrap; }
  .legal { position: absolute; left: 281px; top: 1156px;
    font-family: "Tinos", "Times New Roman", serif; font-size: 17px; letter-spacing: 0.6px;
    color: var(--ink); white-space: nowrap; }
</style>
</head>
<body>
<main class="poster">
  <span class="brand-dot"></span>
  <span class="brand-name">Farwind Treks</span>

  <div class="summary-shape" role="img" aria-label="Grey Tibetan endless knot ornament"></div>
  <p class="summary-text">a 2 week trekking and cultural<br>tour through Ladakh passing<br>over 2 mountain passes in<br>excess of 5000 meters</p>

  <h1>
    <span class="headline-top">Adventure Travel Journey</span>
    <span class="headline-to">to</span>
    <span class="headline-place">Ladakh India</span>
  </h1>
  <p class="season">July and August each year</p>

  <figure class="photo dark photo-peak"><div class="photo-fill" role="img" aria-label="Snow-capped Himalayan peak under cloud"></div></figure>
  <figure class="photo photo-mosque"><div class="photo-fill" role="img" aria-label="White mosque with Leh Palace behind under blue sky"></div></figure>
  <figure class="photo photo-chorten"><div class="photo-fill" role="img" aria-label="Red brick Buddhist stupa spire against sky"></div></figure>
  <figure class="photo photo-gateway"><div class="photo-fill" role="img" aria-label="Wooden gateway framing a whitewashed monastery lane"></div></figure>
  <figure class="photo dark photo-temple"><div class="photo-fill" role="img" aria-label="Colourfully painted Buddhist temple shrine with small stupas"></div></figure>

  <div class="wheel-mark" role="img" aria-label="Dharma wheel emblem"></div>
  <ul class="contact">
    <li>Website: www.farwindtreks.example</li>
    <li>Phone: 01632 960418</li>
    <li>Email: info@farwindtreks.example</li>
  </ul>
  <p class="legal">Farwind Treks is a brand name of Torrent Ridge River Sports LLP</p>
</main>
</body>
</html>
```